Fleeing Marisol Bay website

A very basic website using the graphics provided. The site would give the user the ability to read a description of the book, read testimonials, About the author, Read chapter 1, link to vantoro, order direct via quidlet.

```html
<!DOCTYPE html>
<html lang="en">
<head>
<meta charset="utf-8">
<title>Fleeing Marisol Bay – Testimonials</title>
<link rel="stylesheet" href="https://fonts.googleapis.com/css2?family=Cinzel:wght@400;700&family=Source+Sans+3:wght@300;400&display=swap">
<style>
  :root {
    --bg-deep: #0b0907;
    --wood-mid: #7a2c14;
    --wood-light: #a9451f;
    --band-dark: #1a0a05;
    --gold: #f2b233;
    --gold-deep: #c87d12;
    --gold-muted: #b88a2e;
    --nav-active: #f4b42d;
    --quote-text: #d9d3c8;
    --rust: #c8602a;
    --rust-dark: #6e2a10;
  }
  * { margin: 0; padding: 0; box-sizing: border-box; }
  html, body { width: 1200px; height: 941px; overflow: hidden; background: var(--bg-deep); }
  .page {
    position: relative;
    width: 1200px; height: 941px; overflow: hidden;
    background: radial-gradient(ellipse 700px 500px at 700px 380px, #1d1712 0%, var(--bg-deep) 75%);
  }
  .top-band {
    position: absolute; left: 0; top: 0; width: 1200px; height: 40px;
    background: linear-gradient(180deg, #2a120a 0%, var(--wood-mid) 20%, #4a1c0d 45%, #160805 100%);
  }
  .cover-faces {
    position: absolute; left: 70px; top: 60px; width: 400px; height: 200px;
    background: radial-gradient(ellipse 60px 80px at 80px 90px, #8a4a2a 0%, transparent 100%),
                radial-gradient(ellipse 70px 90px at 200px 100px, #b25a30 0%, transparent 100%),
                radial-gradient(ellipse 60px 85px at 340px 100px, #d8633a 0%, transparent 100%);
    filter: blur(6px);
    opacity: .85;
  }
  .book-box {
    position: absolute; left: 110px; top: 240px; width: 330px; height: 530px;
    background: linear-gradient(100deg, #1b0f12 0%, #3a1a1f 12%, #2a1417 14%, #4a2026 40%, #3a1a20 100%);
    box-shadow: 0 10px 30px rgba(0,0,0,.7);
  }
  .shackle-area {
    position: absolute; left: 404px; top: 645px; width: 126px; height: 175px;
    background: radial-gradient(ellipse 60px 85px at 50% 50%, rgba(80,66,52,.55) 0%, rgba(80,66,52,0) 100%);
  }
  .nav {
    position: absolute; left: 579px; top: 171px;
    display: flex; gap: 14px;
    font-family: "Source Sans 3", sans-serif; font-weight: 300; font-size: 17px;
  }
  .nav a { color: var(--gold-muted); text-decoration: none; }
  .nav a.is-active { color: var(--nav-active); font-weight: 400; }
  .section-title {
    position: absolute; left: 578px; top: 270px;
    font-family: "Cinzel", serif; font-weight: 700; font-size: 68px; letter-spacing: 1.5px;
    text-transform: uppercase;
    background: linear-gradient(180deg, #ffe07a 0%, var(--gold) 45%, var(--gold-deep) 100%);
    -webkit-background-clip: text; background-clip: text; color: transparent;
    line-height: 1;
  }
  .testimonials {
    position: absolute; left: 577px; top: 370px; width: 598px;
    font-family: "Cinzel", serif; font-size: 15.5px; line-height: 18px; letter-spacing: .3px;
    list-style: none;
  }
  .testimonial { margin-bottom: 18px; }
  .testimonial-quote { color: var(--quote-text); text-align: justify; text-align-last: left; }
  .testimonial-source { color: var(--gold-deep); text-align: right; }
  .read-more {
    position: absolute; left: 955px; top: 617px; width: 207px; height: 56px;
    border-radius: 14px;
    background: radial-gradient(ellipse at 50% 40%, #e07a3a 0%, var(--rust) 50%, var(--rust-dark) 100%);
    border: 3px solid #3a1608;
    box-shadow: 0 0 0 2px #a4512a inset;
    display: flex; align-items: center; justify-content: center;
    font-family: "Cinzel", serif; font-weight: 700; font-size: 22px; letter-spacing: 1px;
    color: #3a1a0c; text-decoration: none; text-transform: uppercase;
  }
  .shelf {
    position: absolute; left: 0; top: 716px; width: 1200px; height: 70px;
    background: linear-gradient(180deg, #5a200e 0%, var(--wood-light) 25%, var(--wood-mid) 60%, #3a140a 100%);
  }
  .shelf-edge {
    position: absolute; left: 0; top: 786px; width: 1200px; height: 40px;
    background: linear-gradient(180deg, var(--band-dark) 0%, #3a1409 45%, #120604 100%);
  }
  .footer-band {
    position: absolute; left: 0; top: 826px; width: 1200px; height: 115px;
    background: linear-gradient(180deg, #4a1a0c 0%, #6a2612 50%, #2a0e06 100%);
  }
</style>
</head>
<body>
<div class="page">
  <div class="top-band"></div>

  <div class="cover-faces" role="img" aria-label="Blurred portraits of three women, part of the book artwork"></div>

  <div class="shelf"></div>
  <div class="shelf-edge"></div>
  <div class="footer-band"></div>

  <div class="book-box" role="img" aria-label="3D book box of Fleeing Marisol Bay by Reid Calloway, showing a man silhouetted behind prison bars facing a tropical beach"></div>
  <div class="shackle-area" role="img" aria-label="Open iron shackle resting on the shelf"></div>

  <nav class="nav">
    <a href="#" class="is-active">The Book</a>
    <a href="#">Testimonials</a>
    <a href="#">The Author</a>
    <a href="#">vantoro</a>
    <a href="#">Read Chapter 1</a>
    <a href="#">Order</a>
  </nav>

  <h1 class="section-title">Testimonials</h1>

  <ul class="testimonials">
    <li class="testimonial">
      <p class="testimonial-quote">“This book could easily have been titled, ‘Escapades of a Whoremonger.’ Great stories, very realistic and hard to put down.”</p>
      <p class="testimonial-source">- Walter Brandt, Portland, Oregon</p>
    </li>
    <li class="testimonial">
      <p class="testimonial-quote">“Whether you are a man of fidelity, a man of infidelity, or a man thinking about infidelity, this book is a must read.”</p>
      <p class="testimonial-source">- Dale Hutchins, Atlanta, Georgia</p>
    </li>
    <li class="testimonial">
      <p class="testimonial-quote">“This book confirms why my ex-husband and his buddies frequented Marisol Bay! They were certainly doing more than “fishing.”</p>
      <p class="testimonial-source">- Nora Whitfield Naples, Florida</p>
    </li>
  </ul>

  <a href="#" class="read-more">Read More</a>
</div>
</body>
</html>
```